Harbourline Blinds & Shutters

It Needs to look classy as my target is the upper end of the blind market
I need a Logo design on front and description on back of what i do:
- Roller Blinds
- Vertical Blinds
- Venetian Blinds
- Plantation Shutters
- Aluminum External Shutters
and contact details
Declan
0418275063
and
Trent
0419852306
Updates
Hi Guys,
Sorry for the no feedback but i was waiting on my logo design. But its done now i have uploaded it. so if you could take a look and send through some designs
Reason: my logo was just finished an i just uploaded it today really dont understand why my deadline has been rached foe my bizcards as it states no deadline. But please extend
Target Market(s)
People that live on the coast and are looking for classy good quality blinds and shutters
Font styles to use
Other font styles liked:
- Copperplate Gothic,open to suggestion
Look and feel
Each slider illustrates characteristics of the customer's brand and the style your logo design should communicate.

```html
<!DOCTYPE html>
<html lang="en">
<head>
<meta charset="utf-8">
<title>Harbourline Blinds &amp; Shutters — Business Card</title>
<link rel="stylesheet" href="https://fonts.googleapis.com/css2?family=Quicksand:wght@400;500&display=swap">
<style>
  :root {
    --page-bg: #ffffff;
    --card-black: #0b0b0b;
    --card-charcoal: #1c1c1c;
    --pattern-dark: #141414;
    --pattern-mid: #262626;
    --band-black: #050505;
    --gold: #c9a548;
    --gold-light: #e6cd7a;
    --gold-deep: #8f6f22;
    --silver: #cfcfcf;
    --service-grey: #d4d4d4;
    --card-shadow: rgba(0, 0, 0, 0.28);
  }

  * { box-sizing: border-box; margin: 0; padding: 0; }

  html, body {
    width: 1200px;
    height: 900px;
    overflow: hidden;
    background: var(--page-bg);
  }

  .sheet {
    position: relative;
    width: 1200px;
    height: 900px;
    display: flex;
    align-items: center;
    justify-content: center;
    gap: 40px;
  }

  .card {
    position: relative;
    width: 540px;
    height: 310px;
    border-radius: 22px;
    overflow: hidden;
    box-shadow: 0 14px 30px var(--card-shadow);
    font-family: "Quicksand", "Century Gothic", sans-serif;
  }

  /* Front */
  .card-front { background: var(--card-black); }

  .damask-field {
    position: absolute;
    inset: 0;
    background: radial-gradient(ellipse at 50% 45%, var(--pattern-mid) 0%, var(--pattern-dark) 60%, var(--card-black) 100%);
  }

  .name-band {
    position: absolute;
    left: 0;
    right: 0;
    top: 128px;
    height: 60px;
    background: var(--band-black);
    border-top: 1.5px solid var(--gold);
    border-bottom: 1.5px solid var(--gold);
  }

  .ornament {
    position: absolute;
    left: 50%;
    width: 190px;
    height: 58px;
    transform: translateX(-50%);
    border-radius: 30px;
    background: radial-gradient(ellipse at center, var(--gold-light) 0%, var(--gold) 45%, var(--gold-deep) 80%, transparent 100%);
    opacity: 0.85;
  }
  .ornament-top { top: 58px; }
  .ornament-bottom { top: 198px; }

  .brand-name {
    position: absolute;
    left: 0;
    right: 0;
    top: 120px;
    text-align: center;
    color: var(--silver);
    font-weight: 400;
    line-height: 1;
  }
  .brand-name .brand-main {
    display: block;
    font-size: 46px;
    letter-spacing: 1px;
  }
  .brand-name .brand-sub {
    display: block;
    font-size: 13px;
    letter-spacing: 3px;
    margin-top: 4px;
  }

  /* Back */
  .card-back {
    background: radial-gradient(ellipse at 50% 55%, var(--card-charcoal) 0%, var(--card-black) 70%);
  }

  .contact {
    position: absolute;
    top: 34px;
    color: var(--gold);
    font-weight: 400;
  }
  .contact-left { left: 40px; text-align: center; }
  .contact-right { right: 34px; text-align: center; }

  .contact-name {
    display: block;
    font-size: 19px;
    margin-bottom: 4px;
  }
  .contact-phone {
    display: block;
    font-size: 20px;
    letter-spacing: 1px;
  }

  .services {
    position: absolute;
    left: 0;
    right: 0;
    top: 112px;
    list-style: none;
    text-align: center;
    color: var(--service-grey);
    font-size: 14px;
    line-height: 28px;
  }
</style>
</head>
<body>
  <main class="sheet">
    <section class="card card-front" aria-label="Card front">
      <div class="damask-field" role="img" aria-label="Dark damask floral pattern background"></div>
      <div class="name-band"></div>
      <div class="ornament ornament-top" role="img" aria-label="Gold baroque scroll ornament"></div>
      <div class="ornament ornament-bottom" role="img" aria-label="Gold baroque scroll ornament"></div>
      <h1 class="brand-name">
        <span class="brand-main">Harbourline</span>
        <span class="brand-sub">Blinds &amp; Shutters</span>
      </h1>
    </section>

    <section class="card card-back" aria-label="Card back">
      <div class="contact contact-left">
        <span class="contact-name">Declan</span>
        <span class="contact-phone">0418275063</span>
      </div>
      <div class="contact contact-right">
        <span class="contact-name">Trent</span>
        <span class="contact-phone">0419852306</span>
      </div>
      <ul class="services">
        <li>Roller Blinds</li>
        <li>Vertical Blinds</li>
        <li>Venetian Blinds</li>
        <li>Plantation Shutters</li>
        <li>Aluminum External Shutters</li>
      </ul>
    </section>
  </main>
</body>
</html>
```